Business card design for Automotive workshop

We need a business card for a new automotive repair and tyre shop called Keelstone Prime Automotive located in New Zealand. We are a clean, modern and fresh workshop and company.

Front needs to feature logo,
my name:
Marlo Fitzgerald (director)

Address:
42 Tamsin Road
Harrowby 3592

Phone: 07 541 2298
Mobile: 027 419 5073
Email: office@keelstoneautomotive.co.nz
Website: keelstoneautomotive.co.nz

Back needs to feature an area to write down appointment details, date and time.

Also feature a list of jobs and work we do such as,
Vehicle Servicing
All Mechanical Repairs
Warrant of Fitness
Tyres & Wheel Alignments
Automotive Diagnostics
Automotive Parts & Supplies

```html
<!DOCTYPE html>
<html lang="en">
<head>
<meta charset="utf-8">
<title>Keelstone Prime Automotive – Business Card</title>
<link href="https://fonts.googleapis.com/css2?family=Michroma&family=Roboto:wght@400;500;700&display=swap" rel="stylesheet">
<style>
  :root {
    --bg: #5a6270;
    --card: #0d0d0e;
    --red: #e0141b;
    --white: #ffffff;
    --grey: #d6d6d6;
    --dots: #444;
  }
  * { box-sizing: border-box; margin: 0; padding: 0; }
  html, body { width: 1200px; height: 800px; overflow: hidden; }
  body {
    background: var(--bg);
    font-family: "Roboto", Arial, sans-serif;
    display: flex;
    align-items: center;
    justify-content: center;
    gap: 40px;
  }
  .card {
    width: 540px;
    height: 309px;
    background: var(--card);
    border-bottom: 2px solid var(--red);
    border-left: 1px solid var(--red);
    box-shadow: 0 12px 30px rgba(0,0,0,.35);
    position: relative;
    overflow: hidden;
  }

  /* Front */
  .card-front {
    display: flex;
    flex-direction: column;
    align-items: center;
    justify-content: center;
    text-align: center;
  }
  .person-name {
    font-family: "Michroma", Arial, sans-serif;
    color: var(--red);
    font-size: 17px;
    font-weight: 400;
    letter-spacing: .5px;
  }
  .person-role {
    display: flex;
    align-items: center;
    gap: 6px;
    width: 280px;
    margin-top: 4px;
    font-family: "Michroma", Arial, sans-serif;
    color: var(--grey);
    font-size: 10px;
  }
  .person-role .rule { flex: 1; height: 1px; background: var(--grey); }
  .contact { margin-top: 10px; color: var(--grey); font-size: 10.5px; line-height: 1.6; }
  .contact .label { color: var(--red); }

  /* Back */
  .brand {
    position: absolute;
    left: 34px;
    top: 120px;
    display: flex;
    align-items: center;
    gap: 8px;
  }
  .brand-mark { width: 12px; height: 12px; background: var(--red); }
  .brand-name { color: var(--red); font-weight: 700; font-size: 17px; }

  .services {
    position: absolute;
    left: 300px;
    top: 30px;
    list-style: none;
  }
  .services-title { color: var(--red); font-weight: 700; font-size: 14px; margin-bottom: 3px; }
  .services li.item {
    color: var(--white);
    font-size: 11.5px;
    line-height: 1.55;
    padding-left: 12px;
    position: relative;
  }
  .services li.item::before {
    content: "";
    position: absolute;
    left: 0; top: 7px;
    width: 4px; height: 4px;
    border-radius: 50%;
    background: var(--red);
  }

  .appointment {
    position: absolute;
    left: 36px;
    right: 30px;
    bottom: 26px;
    height: 96px;
    background: var(--white);
    padding: 20px 22px;
    display: flex;
    flex-direction: column;
    justify-content: space-between;
  }
  .appt-row { display: flex; align-items: flex-end; gap: 6px; }
  .appt-label { color: var(--red); font-size: 12px; font-weight: 500; }
  .appt-line { flex: 1; border-bottom: 1px dotted var(--dots); height: 10px; }
  .appt-line.date { flex: 1.6; }
</style>
</head>
<body>
  <section class="card card-front">
    <h1 class="person-name">MARLO FITZGERALD</h1>
    <div class="person-role"><span class="rule"></span>DIRECTOR<span class="rule"></span></div>
    <div class="contact">
      <p>42 Tamsin Road, Harrowby 3592 <span class="label">P.</span> 07 541 2298</p>
      <p><span class="label">C.</span> 027 419 5073 <span class="label">E.</span> office@keelstoneautomotive.co.nz</p>
      <p>www.keelstoneautomotive.co.nz</p>
    </div>
  </section>

  <section class="card card-back">
    <div class="brand">
      <span class="brand-mark"></span>
      <span class="brand-name">Keelstone Prime Automotive</span>
    </div>
    <ul class="services">
      <li class="services-title">VEHICLE SERVICING</li>
      <li class="item">All Mechanical Repairs</li>
      <li class="item">Warrant of Fitness</li>
      <li class="item">Tyres &amp; Wheel Alignments</li>
      <li class="item">Automotive Diagnostics</li>
      <li class="item">Automotive Parts &amp; Supplies</li>
    </ul>
    <div class="appointment">
      <div class="appt-row"><span class="appt-label">Date:</span><span class="appt-line date"></span><span class="appt-label">Time:</span><span class="appt-line"></span></div>
      <div class="appt-row"><span class="appt-label">Date:</span><span class="appt-line date"></span><span class="appt-label">Time:</span><span class="appt-line"></span></div>
    </div>
  </section>
</body>
</html>
```